RM Tomás Ferrier (Business Card)

Hi designers, in this work, I'm looking for an sophisticated stylish, elegant and proffesional personal card. We have a laboratory of pathology automated, with equipments high quality.
In this web the designers, have created my business logo, the name is "RM Tomás Ferrier"
In our lab, we principal work is to prepare the biopsies for further diagnostic of diseases like cancer, tumors, etc.
I need that the first face, only having my complete logo (Rm Tomás Ferrier, Laboratorio de procesamiento Histologico)
The overleaf, could repeat the same logo, like water logo.
In this face, I need to say: My full data:

Técnico en Anatomía Patológica
Tomás Ferrier Bustos M.P 48207
Av. Ramón Quiroga 817 - 2do piso - Instituto Brandeck.
Córdoba, Argentina
(0351) 156284930
ferrier.tomas@correoluz.com

with respect the colors of card, use your imagination, the original logo color is violet, I haven't chosen a color base for the card.

attached pictures are examples of cards I like your DESIGN.
Attached too, the original logo to my company.

the size of card are:
horizontal: 9cm
vertical: 5,5cm

any question that you have, not doubt to question me,
Hand to work!

Industry/Entity Type

Laboratory

Requirements
Must have
• designers sophisticated, not simples, like show the images attached

```html
<!DOCTYPE html>
<html lang="es">
<head>
<meta charset="utf-8">
<title>Tomás Ferrier – Tarjeta personal</title>
<link rel="stylesheet" href="https://fonts.googleapis.com/css2?family=Questrial&family=PT+Sans+Narrow&family=Mulish:wght@700&display=swap">
<style>
  :root {
    --violet: #5e2d8a;
    --grey: #7b7b7e;
    --grey-text: #6d6d70;
    --card-light: #ffffff;
    --card-edge: #dcdcdf;
    --backdrop: #e9e7e4;
    --white: #ffffff;
  }
  * { margin: 0; padding: 0; box-sizing: border-box; }
  html, body { width: 1200px; height: 1181px; overflow: hidden; }
  body { background: var(--backdrop); position: relative; font-family: "Questrial", sans-serif; }

  .card {
    position: absolute; left: 247px; width: 706px; height: 407px;
    background: radial-gradient(ellipse at 50% 45%, var(--card-light) 0%, #f1f1f3 55%, var(--card-edge) 100%);
    box-shadow: 0 6px 14px rgba(0,0,0,.25);
    overflow: hidden;
  }
  .card--front { top: 144px; }
  .card--back { top: 621px; }

  .band-top { position: absolute; top: 0; left: 0; width: 100%; height: 12px; background: var(--violet); }

  .front-footer { position: absolute; bottom: 0; left: 0; width: 100%; height: 12px; display: flex; gap: 3px; }
  .front-footer span { background: var(--violet); flex: 230; }
  .front-footer span.mid { background: var(--grey); flex: 239; }

  .wordmark {
    position: absolute; left: 0; width: 100%; text-align: center;
    font-family: "Questrial", sans-serif; color: var(--violet);
  }
  .card--front .wordmark { top: 172px; font-size: 46px; letter-spacing: 2px; }
  .card--back .wordmark { top: 128px; font-size: 30px; letter-spacing: 6px; text-transform: uppercase; color: var(--grey-text); }

  .rule { position: absolute; left: 188px; width: 325px; top: 179px; height: 1px; background: var(--grey); }
  .tagline {
    position: absolute; top: 184px; left: 0; width: 100%; text-align: center;
    font-family: "PT Sans Narrow", sans-serif; font-size: 25px; color: var(--grey-text);
    text-shadow: 0 1px 1px rgba(0,0,0,.15);
  }

  .back-stripe { position: absolute; left: 0; top: 290px; width: 100%; height: 10px; background: var(--violet); }
  .contact { position: absolute; left: 0; top: 304px; width: 100%; height: 103px; display: flex; gap: 2px; }
  .contact > div {
    display: flex; flex-direction: column; justify-content: center; align-items: center;
    text-align: center; color: var(--white); font-family: "Mulish", sans-serif; font-weight: 700;
    font-size: 12.5px; line-height: 1.25;
  }
  .contact-address, .contact-reach { background: var(--violet); flex: 231; }
  .contact-person { background: var(--grey); flex: 240; padding-bottom: 8px; }
  .contact-person .person-name { font-size: 17px; letter-spacing: .5px; margin-bottom: 3px; }
</style>
</head>
<body>
  <section class="card card--front" aria-label="Frente de la tarjeta">
    <div class="band-top"></div>
    <p class="wordmark">RM Tomás Ferrier</p>
    <div class="front-footer"><span></span><span class="mid"></span><span></span></div>
  </section>

  <section class="card card--back" aria-label="Dorso de la tarjeta">
    <div class="band-top"></div>
    <p class="wordmark">Tomás Ferrier</p>
    <div class="rule"></div>
    <p class="tagline">LABORATORIO DE PROCESAMIENTO HISTOLOGICO</p>
    <div class="back-stripe"></div>
    <div class="contact">
      <div class="contact-address">
        <p>Av. Ramón Quiroga 817 -</p>
        <p>2do piso - Instituto Brandeck.</p>
        <p>Córdoba, Argentina</p>
      </div>
      <div class="contact-person">
        <p class="person-name">Tomás Ferrier Bustos</p>
        <p>Técnico en Anatomía Patológica</p>
        <p>M.P 48207</p>
      </div>
      <div class="contact-reach">
        <p>(0351) 156284930</p>
        <p>ferrier.tomas@correoluz.com</p>
      </div>
    </div>
  </section>
</body>
</html>
```